Tri fold flyer design for restoration company

Use our website for inspiration and make a world class advertising tri fold flyer.
harborlinerecovery.example

Colors
0054AA
0677BA
7BADD7
CADEEF
E8F1F8
00AB8E
00BBA5
67D7C9
C6EFE9
E9F9F6
EB3D1F
EC4F4E
F09395
F8D3D4
FCEDEE

```html
<!DOCTYPE html>
<html lang="en">
<head>
<meta charset="utf-8">
<title>Harborline Recovery – Tri-fold Flyer</title>
<link href="https://fonts.googleapis.com/css2?family=Oswald:wght@300;500;700&family=Montserrat:wght@600;800&family=Open+Sans:ital,wght@0,400;0,600;1,400&display=swap" rel="stylesheet">
<style>
:root{
  --blue:#0054AA;
  --blue-mid:#0677BA;
  --blue-soft:#7BADD7;
  --blue-pale:#CADEEF;
  --blue-mist:#E8F1F8;
  --red:#EB3D1F;
  --red-soft:#EC4F4E;
  --ink:#1d1d1f;
  --grey:#5b6068;
  --paper:#ffffff;
  --bg:#eef1f5;
}
*{box-sizing:border-box;margin:0;padding:0}
html,body{width:1200px;height:2399px;overflow:hidden;background:var(--bg)}
body{position:relative;font-family:"Open Sans",Arial,sans-serif;color:var(--ink)}
.spread{position:absolute;left:30px;width:1140px;height:880px;background:var(--paper);box-shadow:0 10px 30px rgba(20,40,80,.18);overflow:hidden}
.spread--outside{top:250px}
.spread--inside{top:1270px}
.panel{position:absolute;top:0;width:380px;height:880px;overflow:hidden}
.panel--1{left:0}.panel--2{left:380px}.panel--3{left:760px}
.fold{position:absolute;top:0;width:1px;height:880px;background:rgba(0,0,0,.06);z-index:5}
.photo{position:absolute}
.swoosh{position:absolute;left:0;width:100%;overflow:visible}
.brand{font-family:"Montserrat",Arial,sans-serif;font-weight:800;color:var(--blue);display:flex;align-items:center;gap:10px;justify-content:center}
.brand__dot{width:22px;height:22px;border-radius:50%;background:var(--red);flex:none}
.web{font-family:"Montserrat",Arial,sans-serif;font-weight:600;color:var(--ink);text-align:center}
/* outside panel 1 */
.why{position:absolute;left:0;top:0;width:380px;height:600px;background:linear-gradient(160deg,var(--blue) 0%,#1f46b0 100%);color:#fff;padding:34px 30px 0 34px}
.tag{display:inline-block;background:var(--red);color:#fff;font-family:"Oswald",sans-serif;font-weight:700;font-size:17px;padding:3px 14px;border-radius:0 14px 14px 0;margin-left:-34px;padding-left:34px;letter-spacing:.5px}
.why p{font-size:11.5px;font-style:italic;line-height:1.45;margin-top:14px}
.why ul{list-style:none;margin-top:12px}
.why li{font-size:11px;font-style:italic;line-height:1.4;margin-bottom:8px;padding-left:18px;position:relative}
.why li::before{content:"";position:absolute;left:0;top:3px;width:9px;height:9px;border:1.5px solid #fff}
.badges{display:flex;justify-content:space-between;margin-top:16px}
.badge{width:70px;text-align:center;font-size:8.5px;font-style:italic;line-height:1.2}
.badge__shape{width:38px;height:38px;border-radius:50%;background:#fff;margin:0 auto 5px;display:flex;align-items:center;justify-content:center}
.badge__shape span{width:16px;height:16px;border-radius:3px;background:var(--blue)}
.badge__shape--seal span{border-radius:50%;background:var(--blue-soft)}
/* outside panel 2 */
.contact{position:absolute;left:0;top:0;width:380px;height:880px;background:linear-gradient(180deg,#1f46b0 0%,var(--blue) 60%,var(--blue-mid) 100%);color:#fff;text-align:center}
.contact__lead{position:absolute;top:250px;left:40px;right:40px;font-family:"Montserrat",sans-serif;font-weight:600;font-size:15px;letter-spacing:1.5px;line-height:1.4}
.contact__call{position:absolute;top:380px;left:20px;right:20px;font-family:"Oswald",sans-serif;font-weight:500;font-style:italic;font-size:26px;line-height:1.2}
.phone{position:absolute;top:470px;left:50px;right:50px;display:flex;align-items:center;gap:10px;justify-content:center}
.phone__num{border:2px solid #fff;border-radius:20px;padding:2px 18px;font-family:"Montserrat",sans-serif;font-weight:800;font-size:24px;letter-spacing:1px}
.follow{position:absolute;top:560px;left:0;right:0;font-family:"Montserrat",sans-serif;font-weight:600;font-size:14px;letter-spacing:2px}
.social{display:flex;gap:12px;justify-content:center;margin-top:12px}
.social span{width:30px;height:30px;border-radius:50%;border:2px solid #fff}
/* outside panel 3 */
.cover-brand{position:absolute;top:60px;left:0;right:0;font-size:30px}
.tagline{position:absolute;top:712px;left:0;right:0;text-align:center;color:var(--red);font-family:"Oswald",sans-serif;line-height:1.05}
.tagline__light{font-weight:300;font-size:30px;letter-spacing:.5px}
.tagline__bold{font-weight:700;font-size:34px}
.tagline .web{margin-top:10px;font-size:15px}
/* inside */
.heading{font-family:"Oswald",sans-serif;font-weight:700;color:var(--red);line-height:1.05}
.body{font-size:11px;line-height:1.5;color:var(--grey)}
.about{position:absolute;left:32px;right:30px;top:230px}
.about .heading{font-size:25px}
.about .body{margin-top:16px}
.about .body + .body{margin-top:12px}
.services{position:absolute;left:30px;right:28px;top:180px}
.services .heading{font-size:24px;margin-bottom:10px}
.service{display:flex;gap:10px;margin-bottom:10px}
.service__icon{flex:none;width:30px;height:30px;border-radius:50%;background:var(--blue);margin-top:2px;display:flex;align-items:center;justify-content:center}
.pill{display:inline-block;background:var(--blue);color:#fff;font-family:"Oswald",sans-serif;font-weight:500;font-size:14px;padding:2px 16px;border-radius:14px;margin-bottom:6px;letter-spacing:.3px}
.service .pill{margin-bottom:4px;font-size:13px}
.service .body{font-size:10px;line-height:1.45}
.extras{position:absolute;left:28px;right:24px;top:180px}
.extras .heading{font-size:24px;margin-bottom:10px}
.extra{margin-bottom:10px}
.extra .pill{font-size:13px;padding:1px 14px;margin-bottom:4px}
.extra .body{font-size:10px;line-height:1.45}
.extra ol{font-size:10px;color:var(--grey);margin-left:18px;line-height:1.45}
.cta{position:absolute;left:24px;right:20px;top:770px;background:var(--red);color:#fff;border-radius:14px;text-align:center;font-family:"Oswald",sans-serif;font-weight:500;font-size:17px;padding:10px 8px;line-height:1.2}
</style>
</head>
<body>

<section class="spread spread--outside" aria-label="Outside of the tri-fold">
  <div class="panel panel--1">
    <div class="why">
      <span class="tag">WHY CHOOSE US</span>
      <p>At Harborline Recovery we don't believe in doing things by half measures. Our restoration professionals are passionate about helping you get life back to normal quickly. We take pride in delivering exceptional results and making properties look like new again!</p>
      <ul>
        <li>We believe in long-term relationships and provide professional and quick services.</li>
        <li>We have many years of experience in handling disasters in a professional way.</li>
        <li>We are highly trained, equipped with modern equipment and machines, and dedicated to reshape things fast.</li>
        <li>We are available 24/7 to handle any size disaster.</li>
        <li>We have specialized disaster teams that are expert in particular types of disasters.</li>
        <li>We are fast, reliable, dedicated, professional and expert to analyze and handle each situation perfectly.</li>
      </ul>
      <div class="badges">
        <div class="badge"><div class="badge__shape"><span></span></div>24/7 Emergency Service</div>
        <div class="badge"><div class="badge__shape"><span></span></div>Rapid Response Quality Results</div>
        <div class="badge"><div class="badge__shape"><span></span></div>Trained, Certified Service Professionals</div>
        <div class="badge"><div class="badge__shape badge__shape--seal"><span></span></div>Certified Firm</div>
      </div>
    </div>
    <div class="photo" role="img" aria-label="Photo of a bright renovated interior with large windows" style="left:0;top:600px;width:380px;height:150px;background:linear-gradient(180deg,#c9ced6,#eef1f4)"></div>
    <svg class="swoosh" style="top:585px" width="380" height="50" viewBox="0 0 380 50" aria-hidden="true">
      <path d="M0 14 Q190 -4 380 22 L380 30 Q190 6 0 24Z" fill="#1d1d1f"/>
      <path d="M0 24 Q190 6 380 30 L380 40 Q190 16 0 34Z" fill="var(--red)"/>
    </svg>
    <svg class="swoosh" style="top:700px" width="380" height="60" viewBox="0 0 380 60" aria-hidden="true">
      <path d="M0 20 Q200 60 380 10 L380 60 L0 60Z" fill="#fff"/>
      <path d="M0 20 Q200 60 380 10 L380 18 Q200 66 0 28Z" fill="var(--red)"/>
    </svg>
    <div class="brand" style="position:absolute;top:770px;left:0;right:0;font-size:26px"><span class="brand__dot"></span>Harborline Recovery</div>
    <div class="web" style="position:absolute;top:815px;left:0;right:0;font-size:14px">harborlinerecovery.example</div>
  </div>

  <div class="panel panel--2">
    <div class="contact">
      <div class="photo" role="img" aria-label="Black and white photo of two technicians working on a ladder in a room" style="left:0;top:0;width:380px;height:200px;background:linear-gradient(180deg,#e3e5e8,#b9bdc3)"></div>
      <svg class="swoosh" style="top:120px" width="380" height="110" viewBox="0 0 380 110" aria-hidden="true">
        <path d="M0 0 Q40 100 190 96 Q330 92 380 60 L380 110 L0 110Z" fill="#1f46b0"/>
        <path d="M0 0 Q40 100 190 96 Q330 92 380 60 L380 70 Q330 102 190 106 Q30 108 0 20Z" fill="var(--red)"/>
      </svg>
      <div class="contact__lead">OUR CERTIFIED TECHNICIANS WORK WITH ALL INSURANCE CARRIERS</div>
      <div class="contact__call">24/7 EMERGENCY SERVICE<br>CALL NOW!!!</div>
      <div class="phone">
        <svg width="20" height="30" viewBox="0 0 20 30" aria-hidden="true"><rect x="2" y="1" width="16" height="28" rx="3" fill="none" stroke="#fff" stroke-width="2"/><circle cx="10" cy="24" r="1.6" fill="#fff"/></svg>
        <span class="phone__num">(555) 014-2290</span>
      </div>
      <div class="follow">FOLLOW US ON
        <div class="social"><span></span><span></span><span></span></div>
      </div>
      <svg class="swoosh" style="top:780px" width="380" height="100" viewBox="0 0 380 100" aria-hidden="true">
        <path d="M0 30 Q200 70 380 20 L380 100 L0 100Z" fill="#fff"/>
        <path d="M0 30 Q200 70 380 20 L380 30 Q200 80 0 40Z" fill="var(--red)"/>
      </svg>
    </div>
  </div>

  <div class="panel panel--3">
    <div class="brand cover-brand"><span class="brand__dot"></span>Harborline Recovery</div>
    <div class="photo" role="img" aria-label="Photo of a smiling technician in a blue hard hat and overalls on the phone holding plans" style="left:0;top:150px;width:380px;height:540px;background:linear-gradient(160deg,#e9eef4 0%,#9fb6d3 55%,#3b5fa8 100%)"></div>
    <svg class="swoosh" style="top:130px" width="380" height="80" viewBox="0 0 380 80" aria-hidden="true">
      <path d="M0 0 L380 0 L380 20 Q180 30 0 70Z" fill="#fff"/>
      <path d="M380 20 Q180 30 0 70 L0 80 Q180 42 380 30Z" fill="var(--red)"/>
    </svg>
    <svg class="swoosh" style="top:600px" width="380" height="110" viewBox="0 0 380 110" aria-hidden="true">
      <path d="M0 90 Q220 80 380 0 L380 110 L0 110Z" fill="#fff"/>
      <path d="M0 78 Q220 68 380 -10 L380 4 Q220 82 0 92Z" fill="var(--red)"/>
    </svg>
    <div class="tagline">
      <div class="tagline__light">MAKING PROPERTIES</div>
      <div class="tagline__bold">LOOK LIKE NEW AGAIN!</div>
      <div class="web">harborlinerecovery.example</div>
    </div>
  </div>
  <div class="fold" style="left:380px"></div>
  <div class="fold" style="left:760px"></div>
</section>

<section class="spread spread--inside" aria-label="Inside of the tri-fold">
  <div class="photo" role="img" aria-label="Photo of a room with wooden ceiling beams and tall windows" style="left:0;top:0;width:1140px;height:190px;background:linear-gradient(90deg,#5d6670 0%,#a9744a 45%,#c88b55 75%,#8a5a36 100%)"></div>
  <svg class="swoosh" style="top:90px" width="1140" height="140" viewBox="0 0 1140 140" aria-hidden="true">
    <path d="M0 90 Q300 40 560 70 Q860 100 1140 10 L1140 140 L0 140Z" fill="#fff"/>
    <path d="M0 70 Q300 20 560 50 Q860 80 1140 -10 L1140 10 Q860 100 560 70 Q300 40 0 90Z" fill="var(--blue)"/>
    <path d="M760 40 Q960 40 1140 -40 L1140 -20 Q960 60 780 50Z" fill="var(--red)"/>
  </svg>

  <div class="panel panel--1">
    <div class="about">
      <h2 class="heading">We focus on exceptional customer service and satisfaction</h2>
      <p class="body">Our mission at Harborline Recovery is to provide our customers with the highest level of service for all their emergency restoration and cleaning needs, with understanding, integrity and professionalism. Because we are a local cleaning and restoration company, we like to keep our focus on giving back to our community and meeting our customers every day as we go about life. We seek to make our customers feel like more than just another job – we make it our goal to treat our customers like they are our neighbors, friends and family, because that's what they are.</p>
      <p class="body">You will get the highest quality service from our certified and trained staff, and the warmth and kindness you expect from your neighbors, family and friends. Our vision is to become the number one choice and recommended local cleaning and restoration company on the Harbor Coast, partnering with local property managers, realtors, homeowners, insurance companies and business owners to address all of your emergency service and cleaning needs.</p>
    </div>
    <div class="photo" role="img" aria-label="Black and white photo of a technician cleaning a window frame" style="left:0;top:690px;width:380px;height:190px;background:linear-gradient(180deg,#f4f4f4 0%,#9a9a9a 60%,#6f6f6f 100%)"></div>
  </div>

  <div class="panel panel--2">
    <div class="services">
      <h2 class="heading">Residential<br>Commercial Services</h2>
      <div class="service">
        <div class="service__icon"><svg width="16" height="16" viewBox="0 0 16 16" aria-hidden="true"><path d="M8 2 L15 8 H13 V14 H3 V8 H1Z" fill="#fff"/></svg></div>
        <div><span class="pill">WATER DAMAGE</span>
        <p class="body">Water damage is quite common among other disasters. A little amount of water in your home can create a huge loss and damage. This happens when we neglect this little amount of water. It becomes big within a short span of time. The damage that can be caused by water often takes thousands to repair, such as carpets, furniture, wooden floors and lots more.</p></div>
      </div>
      <div class="service">
        <div class="service__icon"><svg width="14" height="16" viewBox="0 0 14 16" aria-hidden="true"><path d="M7 1 C9 5 13 7 13 11 A6 5 0 0 1 1 11 C1 8 4 7 5 4 C6 6 7 6 7 1Z" fill="#fff"/></svg></div>
        <div><span class="pill">FIRE &amp; SMOKE DAMAGE</span>
        <p class="body">Fire incidents are very common and can happen anytime. This experience is very frustrating for home owners and they are not sure what to do in such a disaster. This loss has to be handled very carefully by experts as many materials, equipment, etc. can break, emit toxic gases and make construction weak, among many things they are unaware of.</p></div>
      </div>
      <div class="service">
        <div class="service__icon"><svg width="18" height="12" viewBox="0 0 18 12" aria-hidden="true"><path d="M4 11 A4 4 0 0 1 4 3 A5 5 0 0 1 13 3 A4 4 0 0 1 14 11Z" fill="#fff"/></svg></div>
        <div><span class="pill">WEATHER DAMAGE</span>
        <p class="body">We are not sure of natural calamities that can happen anywhere, anytime. It can be anything like storm, lightning, earthquake that creates a huge loss and damage to properties. These are the situations that are very frustrating, as we don't have the idea or experience to handle them. These need to be handled by experts and professional teams so things can be normal and back in shape as early as possible.</p></div>
      </div>
      <div class="service">
        <div class="service__icon"><svg width="16" height="16" viewBox="0 0 16 16" aria-hidden="true"><circle cx="8" cy="8" r="4" fill="#fff"/><circle cx="3" cy="3" r="1.5" fill="#fff"/><circle cx="13" cy="3" r="1.5" fill="#fff"/><circle cx="3" cy="13" r="1.5" fill="#fff"/><circle cx="13" cy="13" r="1.5" fill="#fff"/></svg></div>
        <div><span class="pill">MOLD</span>
        <p class="body">The development of mold comes with moisture, excessive water, flooding and other types of water leakage. This mold growth is a huge threat to the belongings when it grows. It should be handled at first sight, as it grows at a fast rate and can change the appearance of things. It should be stopped from growing or spreading any further.</p></div>
      </div>
    </div>
  </div>

  <div class="panel panel--3">
    <div class="extras">
      <h2 class="heading">Additional Services</h2>
      <div class="extra"><span class="pill">Crime Scene &amp; Trauma Cleanup</span>
        <ol><li>Safety and Well Being</li><li>Disinfection</li><li>Removal</li><li>Customer Satisfaction</li></ol></div>
      <div class="extra"><span class="pill">Covid-19 Cleaning</span>
        <p class="body">We have all sanitizing tools to give you a germ free environment. We are providing the same by professionals and I am sure you will love it after we are done.</p></div>
      <div class="extra"><span class="pill">Carpet &amp; Furniture Cleaning</span>
        <p class="body">Are you looking for carpet and furniture cleaning service? We are providing the same by professionals and you will love the furniture after we are done.</p></div>
      <div class="extra"><span class="pill">Junk Removal</span>
        <p class="body">Looking for junk removal service on the Harbor Coast? Call us now at (555) 014-2290.</p></div>
      <div class="extra"><span class="pill">Asbestos Removal</span>
        <p class="body">Are you looking for asbestos removal service? We are providing the same by professionals and I am sure you will love the results after we are done.</p></div>
    </div>
    <div class="cta">We are just a call away...call anytime<br>(555) 014-2290</div>
  </div>
  <div class="fold" style="left:380px"></div>
  <div class="fold" style="left:760px"></div>
</section>

</body>
</html>
```